Software Application page - product section

I have developed a proposal generation application and want to improve the main user interface page.
This is the most important and most used page within my application and therefore it needs to look slick, clean, simple and easy to understand whilst looking very professional, creditable and established.
This is the page in which the user makes certain selections of products and the system will in turn display information on the product selected. The user can then add the product to the basket and the system also calculates the monthly cost of the product along with the profit the user makes by offering the particular product.
I have put something together myself and uploaded accordingly to give you an idea as to what it currently looks like and the structure that it needs to follow.
Section 1
This displays the Customer's account, proposal ID, Customer name etc
Section 2
I have these as radio buttons that the user selects, then clicks on the 'Search product' button. The items will then be displayed in section 3
Section 3
This datagrid displays the available products based on the section 2's selections
Section 4
shows information on the product that has been highlighed in section 3's datagrid. The user then clicks in qty field to enter the qty and then clicks the ADD shopping basket button to add the product to the basket in section 5 datagrid.
Section 5
This is the datagrid/shopping basket that displays all the products that the user has added.
Section 6
Displays all the figures including the total qtys', costs, revenue etc
WHILST IT IS IMPORTANT THAT THE DESIGN MUST FOLLOW THE STRUCTURE OF WHAT IS ATTACHED. I MUST POINT OUT THAT I AM NOT HAPPY WITH THE CURRENT DESIGN. I DO NOT LIKE THE LOOK AND FEEL OF THE CURRENT DESIGN AS IT LOOKS CHEAP AND AMATEURISH.
THE RADIO BUTTONS IN SECTION 1 FOR EXAMPLE SHOULD BE MORE CREATIVE, THE SIZE OF EACH SECTIONS CURRENTLY LOOK DISPROPORTIONATE. THE COLOURS ARE ALL OVER THE PLACE.
THE SIZE OF PAGE MUST BE 1009 X 689
PLEASE VISIT OUT OUR WEBSITE TO STICK TO THE COMPANIES BRAND: www.velantix.co.uk
I have other pages within my application that require designs along with icons and a lot of work on the website also require redesigning so the best design will also be given this work
Many thanks
Marcus

```html
<!DOCTYPE html>
<html lang="en">
<head>
<meta charset="utf-8">
<title>Proposal Builder – Product Selection</title>
<link rel="stylesheet" href="https://fonts.googleapis.com/css2?family=Arimo:wght@400;700&display=swap">
<style>
:root{
  --panel:#2f3338;
  --panel-2:#3d4147;
  --gold:#e1bd3b;
  --gold-deep:#c7a536;
  --gold-text:#f0c93a;
  --row-a:#cfcfcf;
  --row-b:#ececec;
  --col-grey:#6b6e72;
  --field:#ffffff;
  --field-grey:#ececec;
  --field-hl:#ffe9a1;
  --well:#d3d3d3;
  --ink:#1b1b1b;
  --white:#ffffff;
}
*{box-sizing:border-box;margin:0;padding:0}
html,body{width:1200px;height:819px;overflow:hidden;background:#fff}
body{font-family:"Arimo",Arial,sans-serif;color:var(--ink)}
.stage{position:relative;width:1009px;height:689px;transform:scale(1.1893);transform-origin:0 0}
.abs{position:absolute}

/* Filters */
.filters{left:6px;top:7px;width:329px;height:301px;background:var(--panel)}
.filter-row{position:absolute;left:0;width:329px;height:49px;border-bottom:1px solid #45494f;display:flex;align-items:center;padding-left:9px;gap:0;color:var(--white);font-size:13px}
.opt{display:flex;align-items:center;gap:6px;margin-right:18px;white-space:nowrap}
.box{width:12px;height:12px;background:var(--white);border:1px solid #9aa0a6;display:inline-flex;align-items:center;justify-content:center}
.search-btn{position:absolute;left:0;top:249px;width:329px;height:52px;background:var(--gold);display:flex}
.search-icon{width:83px;height:52px;background:var(--gold-deep);display:flex;align-items:center;justify-content:center}
.search-label{flex:1;display:flex;align-items:center;justify-content:center;font-size:16px;color:var(--ink)}

/* Grids */
.grid-head{position:absolute;display:flex;color:var(--white);font-size:13px}
.grid-head div{display:flex;align-items:center;justify-content:center}
.row{position:absolute;display:flex;font-size:12.5px}
.tariffs{left:6px;top:316px;width:329px;height:363px;background:var(--panel)}
.tariffs .row:nth-of-type(odd){background:var(--row-a)}
.tariffs .row:nth-of-type(even){background:var(--row-b)}
.scroll-thumb{position:absolute;background:var(--gold)}

/* Product detail */
.detail{left:341px;top:7px;width:180px;height:393px;background:var(--panel)}
.field-label{position:absolute;left:9px;color:var(--white);font-size:11.5px}
.field{position:absolute;left:9px;width:160px;background:var(--field)}
.add-btn{position:absolute;left:9px;top:352px;width:134px;height:33px;background:var(--gold);border-radius:3px;display:flex;overflow:hidden}
.add-icon{width:53px;background:var(--gold-deep);display:flex;align-items:center;justify-content:center}
.add-label{flex:1;display:flex;align-items:center;justify-content:center;font-size:12px}
.info{position:absolute;left:155px;top:349px;color:var(--white);font:italic 700 28px Georgia,serif}
.detail-well{left:341px;top:405px;width:180px;height:274px;background:var(--well)}

/* Proposal header */
.proposal{left:527px;top:7px;width:353px;height:88px;background:var(--panel);color:var(--white);font-size:14px}
.proposal .band{position:absolute;left:0;top:44px;width:353px;height:44px;background:var(--panel-2)}
.kv{position:absolute;left:19px;display:flex}
.kv span:first-child{width:133px}
.brand{left:880px;top:7px;width:121px;height:88px;background:var(--gold-deep);display:flex;align-items:center;justify-content:center;gap:6px;color:var(--white);font-size:17px;font-weight:700}
.brand i{width:10px;height:10px;background:var(--white);display:block}

/* Basket */
.basket{left:527px;top:98px;width:474px;height:339px;background:var(--panel)}
.basket .row div{border-right:1px solid #a9a9a9;height:100%}
.basket .row:nth-of-type(odd){background:var(--row-a)}
.basket .row:nth-of-type(even){background:var(--row-b)}
.delete-bar{left:527px;top:441px;width:395px;height:25px;background:var(--well)}
.delete-btn{left:922px;top:441px;width:78px;height:25px;background:var(--gold-deep);color:var(--white);font-size:13px;display:flex;align-items:center;justify-content:center}

/* Summary */
.summary{left:527px;top:471px;width:474px;height:178px;background:var(--panel);font-size:11.5px;color:var(--white)}
.sum-head{position:absolute;top:2px;height:33px;display:flex;align-items:center;justify-content:center;font-size:13.5px}
.band-row{position:absolute;left:0;width:474px}
.sum-line{position:absolute;left:0;width:474px;display:flex;height:18px;align-items:center}
.sum-line .lbl{width:153px;padding-left:10px}
.sum-line .q{width:66px;text-align:center}
.sum-line .c{width:116px;text-align:center}
.sum-line .r{width:139px;text-align:center;color:var(--gold-text)}
.nav-bar{left:527px;top:653px;width:378px;height:26px;background:var(--well)}
.nav-btn{top:653px;width:46px;height:26px;background:var(--gold-deep);display:flex;align-items:center;justify-content:center}
</style>
</head>
<body>
<div class="stage">

  <!-- Section 2: filters -->
  <section class="abs filters" aria-label="Product filters">
    <div class="filter-row" style="top:0">
      <label class="opt"><span class="box"><svg width="10" height="10" viewBox="0 0 10 10"><path d="M1.5 5.2l2.3 2.4 4.7-5.4" fill="none" stroke="#2a8a3a" stroke-width="1.8"/></svg></span>Mobile</label>
      <label class="opt"><span class="box"></span>Fixed Line</label>
      <label class="opt"><span class="box"></span>Other Products</label>
    </div>
    <div class="filter-row" style="top:49px">
      <label class="opt"><span class="box"><svg width="10" height="10" viewBox="0 0 10 10"><path d="M1.5 5.2l2.3 2.4 4.7-5.4" fill="none" stroke="#2a8a3a" stroke-width="1.8"/></svg></span>Nova</label>
      <label class="opt"><span class="box"></span>Vantel</label>
      <label class="opt"><span class="box"></span>Exa</label>
      <label class="opt"><span class="box"></span>Amberline</label>
    </div>
    <div class="filter-row" style="top:99px">
      <label class="opt"><span class="box"><svg width="10" height="10" viewBox="0 0 10 10"><path d="M1.5 5.2l2.3 2.4 4.7-5.4" fill="none" stroke="#2a8a3a" stroke-width="1.8"/></svg></span>New</label>
      <label class="opt" style="margin-left:16px"><span class="box"></span>Resign</label>
    </div>
    <div class="filter-row" style="top:149px">
      <label class="opt" style="margin-right:10px"><span class="box"><svg width="10" height="10" viewBox="0 0 10 10"><path d="M1.5 5.2l2.3 2.4 4.7-5.4" fill="none" stroke="#2a8a3a" stroke-width="1.8"/></svg></span>12</label>
      <label class="opt" style="margin-right:10px"><span class="box"></span>24</label>
      <label class="opt" style="margin-right:10px"><span class="box"></span>36</label>
      <label class="opt" style="margin-right:10px"><span class="box"></span>48</label>
      <label class="opt" style="margin-right:10px"><span class="box"></span>60</label>
      <label class="opt" style="margin-right:0"><span class="box"></span>Other</label>
    </div>
    <div class="filter-row" style="top:199px">
      <label class="opt" style="margin-right:8px"><span class="box"><svg width="10" height="10" viewBox="0 0 10 10"><path d="M1.5 5.2l2.3 2.4 4.7-5.4" fill="none" stroke="#2a8a3a" stroke-width="1.8"/></svg></span>Share Plan</label>
      <label class="opt" style="margin-right:8px"><span class="box"></span>Single Plan</label>
      <label class="opt" style="margin-right:8px"><span class="box"></span>MBB</label>
      <label class="opt" style="margin-right:0"><span class="box"></span>Add-0n</label>
    </div>
    <div class="search-btn">
      <div class="search-icon">
        <svg width="34" height="30" viewBox="0 0 34 30"><circle cx="12" cy="11" r="8" fill="none" stroke="#fff" stroke-width="3"/><path d="M18 17l11 9" stroke="#fff" stroke-width="4.5" stroke-linecap="round"/></svg>
      </div>
      <div class="search-label">Search Product</div>
    </div>
  </section>

  <!-- Section 3: available tariffs -->
  <section class="abs tariffs" aria-label="Available tariffs">
    <div class="grid-head" style="left:4px;top:2px;height:23px;width:313px">
      <div style="width:232px">Tariff</div>
      <div style="width:81px;background:#595c60">Price</div>
    </div>
    <div class="row" style="left:4px;top:27px;width:313px;height:25px"><div style="width:232px;padding:4px 8px">Business Single 300</div><div style="width:81px;padding-top:5px;text-align:center;font-size:11.5px">19.03</div></div>
    <div class="row" style="left:4px;top:52px;width:313px;height:25px"><div style="width:232px;padding:4px 8px">Business Single 600</div><div style="width:81px;padding-top:5px;text-align:center;font-size:11.5px">25.09</div></div>
    <div class="row" style="left:4px;top:77px;width:313px;height:25px"><div style="width:232px;padding:4px 8px">Best for Business PAYU</div><div style="width:81px;padding-top:5px;text-align:center;font-size:11.5px">12.56</div></div>
    <div class="row" style="left:4px;top:102px;width:313px;height:25px"><div style="width:232px;padding:4px 8px">Best for Business PAYU Unlimited</div><div style="width:81px;padding-top:5px;text-align:center;font-size:11.5px">22.75</div></div>
    <div class="row" style="left:4px;top:127px;width:313px;height:25px"><div style="width:232px;padding:4px 8px">Business Single 50</div><div style="width:81px;padding-top:5px;text-align:center;font-size:11.5px">12.11</div></div>
    <div class="row" style="left:4px;top:152px;width:313px;height:25px"><div style="width:232px;padding:4px 8px">Business Single on &amp;plus</div><div style="width:81px;padding-top:5px;text-align:center;font-size:11.5px">32.14</div></div>
    <div class="row" style="left:4px;top:177px;width:313px;height:25px"><div style="width:232px;padding:4px 8px">Business Single on &amp;plus</div><div style="width:81px;padding-top:5px;text-align:center;font-size:11.5px">25.09</div></div>
    <div class="row" style="left:4px;top:202px;width:313px;height:25px"><div style="width:232px;padding:4px 8px">Business Single on &amp;plus</div><div style="width:81px;padding-top:5px;text-align:center;font-size:11.5px">12.56</div></div>
    <div class="row" style="left:4px;top:227px;width:313px;height:25px"><div style="width:232px;padding:4px 8px">Business Single on &amp;plus</div><div style="width:81px;padding-top:5px;text-align:center;font-size:11.5px">22.75</div></div>
    <div class="row" style="left:4px;top:252px;width:313px;height:25px"><div style="width:232px;padding:4px 8px">Business Single on &amp;plus</div><div style="width:81px;padding-top:5px;text-align:center;font-size:11.5px">12.11</div></div>
    <div class="row" style="left:4px;top:277px;width:313px;height:25px"><div style="width:232px;padding:4px 8px">Business Single on &amp;plus</div><div style="width:81px;padding-top:5px;text-align:center;font-size:11.5px">32.14</div></div>
    <div class="row" style="left:4px;top:302px;width:313px;height:25px"><div style="width:232px;padding:4px 8px">Business Single on &amp;plus</div><div style="width:81px;padding-top:5px;text-align:center;font-size:11.5px">32.14</div></div>
    <div class="row" style="left:4px;top:327px;width:313px;height:25px"><div style="width:232px;padding:4px 8px">Business Single on &amp;plus</div><div style="width:81px;padding-top:5px;text-align:center;font-size:11.5px">32.14</div></div>
    <div class="scroll-thumb" style="left:320px;top:67px;width:6px;height:64px"></div>
    <div class="scroll-thumb" style="left:58px;top:355px;width:33px;height:5px"></div>
  </section>

  <!-- Section 4: product detail -->
  <section class="abs detail" aria-label="Product detail">
    <span class="field-label" style="top:19px">Product</span>
    <div class="field" style="top:33px;height:34px;background:var(--field-grey)"></div>
    <span class="field-label" style="top:72px">Qty</span>
    <div class="field" style="top:86px;height:22px"></div>
    <span class="field-label" style="top:113px">Tariff Cost</span>
    <div class="field" style="top:127px;height:22px"></div>
    <span class="field-label" style="top:154px">Revenue %</span>
    <div class="field" style="top:168px;height:22px;background:var(--field-hl)"></div>
    <span class="field-label" style="top:195px">Minutes</span>
    <div class="field" style="top:209px;height:22px"></div>
    <span class="field-label" style="top:236px">Texts</span>
    <div class="field" style="top:250px;height:22px"></div>
    <span class="field-label" style="top:277px">Data</span>
    <div class="field" style="top:291px;height:52px;background:#d2d2d2"></div>
    <div class="add-btn">
      <div class="add-icon">
        <svg width="44" height="24" viewBox="0 0 44 24"><path d="M2 12h9M6.5 7.5v9" stroke="#fff" stroke-width="2.5"/><path d="M14 4h4l3 13h16l3-10H19" fill="none" stroke="#fff" stroke-width="1.8"/><path d="M22 10h15M23 13.5h13" stroke="#fff" stroke-width="1"/><circle cx="23" cy="21" r="1.8" fill="#fff"/><circle cx="35" cy="21" r="1.8" fill="#fff"/></svg>
      </div>
      <div class="add-label">Add Product</div>
    </div>
    <span class="info">i</span>
  </section>
  <div class="abs detail-well"></div>

  <!-- Section 1: proposal header -->
  <header class="abs proposal" aria-label="Proposal details">
    <div class="band"></div>
    <div class="kv" style="top:5px"><span>Proposal ID :</span><span>1334235</span></div>
    <div class="kv" style="top:25px"><span>Status :</span><span style="color:var(--gold-text)">Incomplete</span></div>
    <div class="kv" style="top:49px"><span>Customer ID :</span><span>110399</span></div>
    <div class="kv" style="top:69px"><span>Customer Name :</span><span>Velantix Test Ltd</span></div>
  </header>
  <div class="abs brand"><i></i>Velantix</div>

  <!-- Section 5: basket -->
  <section class="abs basket" aria-label="Basket">
    <div class="grid-head" style="left:6px;top:2px;height:25px;width:456px;font-size:14px">
      <div style="width:214px">Tariff</div>
      <div style="width:54px;background:var(--col-grey)">Type</div>
      <div style="width:66px">Price</div>
      <div style="width:55px;background:var(--col-grey)">QTY</div>
      <div style="width:67px">Total</div>
    </div>
    <div class="row" style="left:6px;top:29px;width:456px;height:25px"><div style="width:215px"></div><div style="width:54px"></div><div style="width:66px"></div><div style="width:55px"></div><div style="width:66px;border:0"></div></div>
    <div class="row" style="left:6px;top:54px;width:456px;height:25px"><div style="width:215px"></div><div style="width:54px"></div><div style="width:66px"></div><div style="width:55px"></div><div style="width:66px;border:0"></div></div>
    <div class="row" style="left:6px;top:79px;width:456px;height:25px"><div style="width:215px"></div><div style="width:54px"></div><div style="width:66px"></div><div style="width:55px"></div><div style="width:66px;border:0"></div></div>
    <div class="row" style="left:6px;top:104px;width:456px;height:25px"><div style="width:215px"></div><div style="width:54px"></div><div style="width:66px"></div><div style="width:55px"></div><div style="width:66px;border:0"></div></div>
    <div class="row" style="left:6px;top:129px;width:456px;height:25px"><div style="width:215px"></div><div style="width:54px"></div><div style="width:66px"></div><div style="width:55px"></div><div style="width:66px;border:0"></div></div>
    <div class="row" style="left:6px;top:154px;width:456px;height:25px"><div style="width:215px"></div><div style="width:54px"></div><div style="width:66px"></div><div style="width:55px"></div><div style="width:66px;border:0"></div></div>
    <div class="row" style="left:6px;top:179px;width:456px;height:25px"><div style="width:215px"></div><div style="width:54px"></div><div style="width:66px"></div><div style="width:55px"></div><div style="width:66px;border:0"></div></div>
    <div class="row" style="left:6px;top:204px;width:456px;height:25px"><div style="width:215px"></div><div style="width:54px"></div><div style="width:66px"></div><div style="width:55px"></div><div style="width:66px;border:0"></div></div>
    <div class="row" style="left:6px;top:229px;width:456px;height:25px"><div style="width:215px"></div><div style="width:54px"></div><div style="width:66px"></div><div style="width:55px"></div><div style="width:66px;border:0"></div></div>
    <div class="row" style="left:6px;top:254px;width:456px;height:25px"><div style="width:215px"></div><div style="width:54px"></div><div style="width:66px"></div><div style="width:55px"></div><div style="width:66px;border:0"></div></div>
    <div class="row" style="left:6px;top:279px;width:456px;height:25px"><div style="width:215px"></div><div style="width:54px"></div><div style="width:66px"></div><div style="width:55px"></div><div style="width:66px;border:0"></div></div>
    <div class="row" style="left:6px;top:304px;width:456px;height:23px"><div style="width:215px"></div><div style="width:54px"></div><div style="width:66px"></div><div style="width:55px"></div><div style="width:66px;border:0"></div></div>
    <div class="scroll-thumb" style="left:465px;top:72px;width:6px;height:70px"></div>
    <div class="scroll-thumb" style="left:73px;top:330px;width:44px;height:5px"></div>
  </section>
  <div class="abs delete-bar"></div>
  <div class="abs delete-btn">Delete</div>

  <!-- Section 6: totals -->
  <section class="abs summary" aria-label="Totals">
    <div class="sum-head" style="left:153px;width:66px;background:#54575b">Qty</div>
    <div class="sum-head" style="left:219px;width:116px">Monthly Cost</div>
    <div class="sum-head" style="left:335px;width:139px;background:#54575b;color:var(--gold-text)">Monthly Revenue</div>
    <div class="band-row" style="top:37px;height:56px;background:#6a6d71"></div>
    <div class="band-row" style="top:94px;height:19px;background:#82868b"></div>
    <div class="band-row" style="top:115px;height:19px;background:#82868b"></div>
    <div class="sum-line" style="top:38px"><span class="lbl">Mobile Voice</span><span class="q">0</span><span class="c">0</span><span class="r">0</span></div>
    <div class="sum-line" style="top:56px"><span class="lbl">Mobile Data Only</span><span class="q">0</span><span class="c">0</span><span class="r">0</span></div>
    <div class="sum-line" style="top:74px"><span class="lbl">Mobile Total</span><span class="q">0</span><span class="c">0</span><span class="r">0</span></div>
    <div class="sum-line" style="top:95px"><span class="lbl">Fixed Line</span><span class="q">-</span><span class="c">0</span><span class="r">0</span></div>
    <div class="sum-line" style="top:115px"><span class="lbl">Other Products</span><span class="q">-</span><span class="c">0</span><span class="r">0</span></div>
    <div class="sum-line" style="top:139px"><span class="lbl">Total Monthly Cost</span><span class="q">-</span><span class="c">0</span><span class="r" style="color:var(--white)">-</span></div>
    <div class="sum-line" style="top:157px"><span class="lbl" style="color:var(--gold-text)">Total Monthly Revenue</span><span class="q">-</span><span class="c">-</span><span class="r">99999.00</span></div>
  </section>

  <div class="abs nav-bar"></div>
  <div class="abs nav-btn" style="left:907px" aria-label="Previous">
    <svg width="16" height="18" viewBox="0 0 16 18"><path d="M12 2L4 9l8 7" fill="none" stroke="#fff" stroke-width="2.6"/></svg>
  </div>
  <div class="abs nav-btn" style="left:955px" aria-label="Next">
    <svg width="16" height="18" viewBox="0 0 16 18"><path d="M4 2l8 7-8 7" fill="none" stroke="#fff" stroke-width="2.6"/></svg>
  </div>

</div>
</body>
</html>
```